Condo Debts Collection Business needs a Web Design (Contest)

I need a site for a client, who works with condo debts collection, and ensure all revenues provided by condo fees will be always available to the building manager of condo on a specific date, regardless of defaults.I have the logo of the companies, and some requirements on layout (kind of slider, menu options, phone number on a noble position, etc).
Updates

Designs look the same

Target Market(s)

I have two targets for this design: - Condominium's building manager. This target is looking for a solution to overdue debts on it's condo. - Residents on condominiums. This target wants to live in a better place, where their neighbors pay their condominium fees on time.

Number of Pages Required

1 page

Requirements
Must have
• - Slider with title, some short text related, a nice image (I prefer happy and/or peaceful family, people doing business, happy friends, and so on).
• - I have a special attention to menu. I'm looking for one I can have a nice effect, more elegant, charming, kind of innovative.
• - Phone number on the top (or clearly visible).
• - Member log in area or icon on the top (or clearly visible).
• - News/articles area.
• - Modern fonts, with good quality, sans-serif on areas where reading is more intensive (prefer Google web-fonts).
• - Colors specified on attached files.
• - Header similar or inspired by the "FILE 3"
Nice to have
• - Clear background color, cause it's better to read larger texts (like articles). Dark backgrounds makes reading difficult.
• - A site with effects (like shadows, lines, gradients, lights) is usually pretty.
• - I pay attention on beautiful footers.
Should not have
• - Images with a lot of money (I don't sell richness, I sell tranquility, peace, harmony, safety).
• - Poor menu.
• - Lots of curves. My customer asked for straight lines.

```html
<!DOCTYPE html>
<html lang="en">
<head>
<meta charset="utf-8">
<title>Serenova – Condo Debts Collection</title>
<link rel="stylesheet" href="https://fonts.googleapis.com/css2?family=Poppins:wght@500;600;700;800;900&family=Open+Sans:wght@400;600;700&display=swap">
<style>
:root{
  --navy:#0f2b5e;
  --navy-deep:#0a2150;
  --orange:#e8601c;
  --orange-soft:#f08a3c;
  --paper:#f3f1f1;
  --white:#ffffff;
  --ink:#333a45;
  --muted:#6b7280;
}
*{box-sizing:border-box;margin:0;padding:0}
html,body{width:1200px;height:3991px;overflow:hidden}
body{font-family:"Open Sans",sans-serif;color:var(--ink);background:var(--white);position:relative}
section,header,footer{position:relative;width:1200px}
.abs{position:absolute}
.heading{font-family:"Poppins",sans-serif;font-weight:900;color:var(--navy);text-align:center;font-size:38px;letter-spacing:.5px}
.dots{display:flex;gap:3px;justify-content:center}
.dots span{width:5px;height:5px;background:var(--orange)}
.dots.two span{}
.btn{display:inline-block;background:var(--orange);color:#fff;font-family:"Poppins",sans-serif;font-weight:700;text-transform:uppercase;text-align:center}

/* HERO */
.hero{height:650px;overflow:hidden}
.hero-photo{position:absolute;inset:0;background:linear-gradient(180deg,#f7e7c2 0%,#f0c77a 30%,#d98f3a 55%,#8a5a2a 80%,#5a3a1d 100%)}
.hero-glow{position:absolute;left:200px;top:60px;width:600px;height:420px;background:radial-gradient(closest-side,rgba(255,244,210,.9),rgba(255,244,210,0))}
.brand{left:140px;top:22px;width:220px}
.brand-name{display:flex;align-items:center;gap:8px;font-family:"Poppins",sans-serif;font-weight:800;font-size:30px;color:var(--navy);margin-top:88px}
.brand-name i{width:16px;height:16px;background:var(--orange);display:block}
.brand-tag{font-size:9px;color:var(--orange);font-weight:600;margin-top:2px}
.call{left:662px;top:30px;display:flex;align-items:center;gap:10px}
.call .ring{width:34px;height:34px;border-radius:50%;background:var(--navy);display:flex;align-items:center;justify-content:center}
.call small{display:block;font-size:11px;font-weight:700;color:var(--navy);letter-spacing:.5px}
.call strong{display:block;font-family:"Poppins",sans-serif;font-size:25px;font-weight:700;color:var(--orange);line-height:1}
.login{left:900px;top:28px;width:155px;height:40px;line-height:40px;font-size:12px}
.nav{left:488px;top:100px;display:flex;gap:32px;font-family:"Poppins",sans-serif;font-weight:700;font-size:13px;color:var(--navy)}
.nav a{color:inherit;text-decoration:none}
.nav a.active{color:var(--orange)}
.hero-title{left:838px;top:268px;font-family:"Poppins",sans-serif;font-weight:900;font-size:39px;line-height:1.08;color:var(--navy)}
.hero-btn{left:845px;top:380px;width:118px;height:40px;line-height:40px;font-size:12px}
.slider-dots{left:545px;top:593px;display:flex;gap:16px}
.slider-dots span{width:10px;height:10px;border-radius:50%;background:#fff;opacity:.85}
.slider-dots span.on{background:transparent;border:2px solid #fff}

/* SERVICES */
.services{height:866px;background:var(--paper)}
.services .heading{position:absolute;top:700px;}
.services .heading{top:50px;width:100%}
.services .dots{position:absolute;top:115px;width:100%}
.corner-tr{left:990px;top:170px}
.corner-bl{left:140px;top:740px}
.service-grid{position:absolute;left:163px;top:180px;display:grid;grid-template-columns:repeat(3,283px);gap:14px 12px}
.service-card{height:302px;background:#fff;box-shadow:0 4px 14px rgba(0,0,0,.08);text-align:center;padding:30px 28px 0}
.service-icon{width:82px;height:82px;border-radius:50%;background:var(--orange);margin:0 auto 14px;display:flex;align-items:center;justify-content:center}
.service-card h3{font-family:"Poppins",sans-serif;font-weight:700;font-size:15px;color:var(--navy);line-height:1.15;min-height:36px;display:flex;align-items:center;justify-content:center}
.service-card p{font-size:12.5px;line-height:1.45;margin-top:10px;color:#333}

/* ABOUT */
.about{height:650px;background:#fff}
.about-photo{left:140px;top:80px;width:395px;height:490px;background:linear-gradient(135deg,#6fa8d8 0%,#3d6f9e 40%,#2c3f55 75%,#1e2630 100%);box-shadow:-12px 12px 0 #f0eeee}
.about-kicker{left:597px;top:78px;font-family:"Poppins",sans-serif;font-weight:700;font-size:22px;color:var(--navy)}
.about-title{left:597px;top:110px;font-family:"Poppins",sans-serif;font-weight:900;font-size:45px;color:var(--navy);letter-spacing:.5px}
.about .dots{left:600px;top:172px;justify-content:flex-start}
.about-text{left:600px;top:205px;width:370px;font-size:13.5px;line-height:1.5}
.features{left:600px;top:350px;display:grid;grid-template-columns:repeat(3,155px);width:465px}
.feature{height:104px;text-align:center;padding-top:12px;border-right:1px solid #e3e3e3}
.feature:nth-child(3n){border-right:none}
.feature:nth-child(-n+3){border-bottom:1px solid #e3e3e3}
.feature b{display:block;margin-top:10px;font-family:"Poppins",sans-serif;font-weight:600;font-size:14px;color:var(--navy)}

/* ARTICLES */
.articles{height:634px;background:var(--paper)}
.articles .heading{position:absolute;top:48px;width:100%}
.articles .dots{position:absolute;top:113px;width:100%}
.article-grid{position:absolute;left:137px;top:175px;display:grid;grid-template-columns:repeat(3,288px);gap:32px}
.article-card{height:395px;background:#fff;box-shadow:0 4px 14px rgba(0,0,0,.08);position:relative}
.article-img{height:202px}
.a1{background:linear-gradient(180deg,#f5d58e,#e69a47 55%,#7a4a22)}
.a2{background:linear-gradient(180deg,#cfe3f5,#6a8fb5 55%,#1d2c40)}
.a3{background:linear-gradient(180deg,#e8ebee,#a9b3bd 55%,#535c66)}
.article-date{position:absolute;left:20px;top:186px;background:#fff;font-size:10.5px;padding:6px 10px}
.article-body{padding:28px 24px 0}
.article-body h3{font-family:"Poppins",sans-serif;font-weight:700;font-size:14.5px;line-height:1.3;color:#111}
.article-body p{font-size:12px;line-height:1.45;margin-top:10px}
.article-body .btn{margin-top:16px;width:86px;height:26px;line-height:26px;font-size:10px}

/* TESTIMONIALS */
.testimonials{height:477px;background:#fff}
.testimonials .heading{position:absolute;top:82px;width:100%}
.testimonials .dots{position:absolute;top:143px;width:100%}
.quote-open{left:312px;top:165px;font-family:"Poppins",sans-serif;font-size:80px;color:#bbb;line-height:1}
.quote-close{left:795px;top:325px;font-family:"Poppins",sans-serif;font-size:80px;color:#bbb;line-height:1}
.quote{left:330px;top:190px;width:540px;text-align:center;font-size:14px;line-height:1.5}
.who{left:0;width:1200px;top:364px;text-align:center;font-size:12px}
.who b{display:block;font-weight:700;font-size:12.5px;color:#111}
.arrow-l{left:140px;top:238px}
.arrow-r{left:1035px;top:238px}

/* CTA */
.cta{height:333px;background:linear-gradient(180deg,#eef0f4,#dfe3ea);overflow:hidden}
.cta-photo{position:absolute;inset:0;background:radial-gradient(ellipse at 40% 50%,rgba(160,170,185,.35),rgba(255,255,255,0) 60%)}
.cta-line1{left:0;width:1200px;top:92px;text-align:center;font-family:"Poppins",sans-serif;font-weight:600;font-size:30px;color:var(--navy)}
.cta-line2{left:0;width:1200px;top:136px;text-align:center;font-size:31px;color:var(--navy)}
.cta .btn{left:512px;top:200px;width:178px;height:52px;line-height:52px;font-size:17px}

/* FOOTER */
.footer{height:381px;background:linear-gradient(135deg,#0b2657,#0f2f6a 60%,#143a7e);color:#fff;overflow:hidden}
.footer-deco{right:0;top:40px}
.footer-brand{left:125px;top:32px;width:255px;height:240px;background:rgba(255,255,255,.05);display:flex;flex-direction:column;align-items:center;justify-content:center}
.footer-brand .brand-name{color:#fff;margin-top:60px;font-size:30px}
.footer-brand .brand-tag{color:var(--orange-soft)}
.fcol{top:75px;font-size:11px;line-height:1.7}
.fcol h4{font-family:"Poppins",sans-serif;font-weight:700;font-size:12px;margin-bottom:14px;letter-spacing:.3px}
.fcol .row{display:flex;gap:12px;align-items:flex-start;margin-bottom:12px}
.fcol .soc{display:flex;align-items:center;gap:10px;margin-bottom:12px}
.soc i{width:22px;height:22px;border-radius:50%;background:#fff;display:block}
.footer-rule{left:446px;top:285px;width:740px;height:1px;background:rgba(255,255,255,.25)}
.copyright{left:0;width:1200px;top:335px;text-align:center;font-size:11px}
</style>
</head>
<body>

<header class="hero">
  <div class="hero-photo" role="img" aria-label="Happy family running hand in hand through a golden field at sunset"></div>
  <div class="hero-glow"></div>
  <div class="abs brand">
    <div class="brand-name"><i></i>SERENOVA</div>
    <div class="brand-tag">Your guarantee of calm</div>
  </div>
  <div class="abs call">
    <div class="ring"><svg width="16" height="16" viewBox="0 0 24 24"><path fill="#fff" d="M6.6 10.8a15 15 0 006.6 6.6l2.2-2.2c.3-.3.7-.4 1-.2 1.1.4 2.3.6 3.6.6.6 0 1 .4 1 1V20c0 .6-.4 1-1 1A17 17 0 013 4c0-.6.4-1 1-1h3.5c.6 0 1 .4 1 1 0 1.3.2 2.5.6 3.6.1.3 0 .7-.2 1z"/></svg></div>
    <div><small>CALL US NOW</small><strong>800.555.0199</strong></div>
  </div>
  <a class="abs btn login">Member Log In</a>
  <nav class="abs nav">
    <a class="active">HOME</a><a>ABOUT US</a><a>SERVICES</a><a>COMPLIANCE</a><a>BLOG</a><a>CONTACT US</a>
  </nav>
  <h1 class="abs hero-title">CONDO DEBTS<br>COLLECTION</h1>
  <a class="abs btn hero-btn">Read More</a>
  <div class="abs slider-dots"><span></span><span></span><span class="on"></span><span></span><span></span></div>
</header>

<section class="services">
  <h2 class="heading">OUR SERVICES</h2>
  <div class="dots"><span></span><span></span><span></span><span></span><span></span><span></span></div>
  <svg class="abs corner-tr" width="56" height="56"><polygon points="0,0 56,0 56,56 40,56 40,16 0,16" fill="var(--navy)"/></svg>
  <svg class="abs corner-bl" width="76" height="80"><polygon points="0,0 16,0 16,64 76,64 76,80 0,80" fill="var(--navy)"/><polygon points="0,30 50,80 0,80" fill="var(--navy)"/></svg>
  <div class="service-grid">
    <article class="service-card">
      <div class="service-icon"><svg width="40" height="40" viewBox="0 0 40 40" fill="none" stroke="#fff" stroke-width="2.5"><circle cx="24" cy="12" r="8"/><path d="M4 28h8l8 4h10l6-6"/></svg></div>
      <h3>Commercial<br>Debt Collections</h3>
      <p>Lorem ipsum dolor sit amet, consectetur adipiscing elit, sed do eiusmod tempor incididunt ut sed quia non numquam eius modi tempora.</p>
    </article>
    <article class="service-card">
      <div class="service-icon"><svg width="36" height="40" viewBox="0 0 36 40" fill="none" stroke="#fff" stroke-width="2.5"><rect x="5" y="5" width="26" height="32"/><path d="M11 14h14M11 20h14M11 26h14"/></svg></div>
      <h3>Default listing</h3>
      <p>Lorem ipsum dolor sit amet, consectetur adipiscing elit, sed do eiusmod tempor incididunt ut sed quia non numquam eius modi tempora.</p>
    </article>
    <article class="service-card">
      <div class="service-icon"><svg width="40" height="40" viewBox="0 0 40 40" fill="none" stroke="#fff" stroke-width="2.5"><rect x="4" y="4" width="12" height="12"/><rect x="24" y="4" width="12" height="12"/><rect x="4" y="24" width="12" height="12"/><rect x="24" y="24" width="12" height="12"/></svg></div>
      <h3>Full Legal Process</h3>
      <p>Lorem ipsum dolor sit amet, consectetur adipiscing elit, sed do eiusmod tempor incididunt ut sed quia non numquam eius modi tempora.</p>
    </article>
    <article class="service-card">
      <div class="service-icon"><svg width="40" height="40" viewBox="0 0 40 40" fill="#fff"><circle cx="20" cy="13" r="7"/><rect x="8" y="23" width="24" height="12"/></svg></div>
      <h3>Consumer<br>Debt Collections</h3>
      <p>Lorem ipsum dolor sit amet, consectetur adipiscing elit, sed do eiusmod tempor incididunt ut sed quia non numquam eius modi tempora.</p>
    </article>
    <article class="service-card">
      <div class="service-icon"><svg width="42" height="40" viewBox="0 0 42 40" fill="none" stroke="#fff" stroke-width="2.5"><rect x="4" y="6" width="34" height="22"/><path d="M16 34h10M21 28v6M9 22l8-7 6 4 9-8"/></svg></div>
      <h3>Monitoring of Debtors</h3>
      <p>Lorem ipsum dolor sit amet, consectetur adipiscing elit, sed do eiusmod tempor incididunt ut sed quia non numquam eius modi tempora.</p>
    </article>
    <article class="service-card">
      <div class="service-icon"><svg width="40" height="40" viewBox="0 0 40 40" fill="none" stroke="#fff" stroke-width="2.5"><circle cx="20" cy="15" r="8"/><path d="M8 36c2-7 6-10 12-10s10 3 12 10M10 15h-3v6h3M30 15h3v6h-3"/></svg></div>
      <h3>Customer service</h3>
      <p>Lorem ipsum dolor sit amet, consectetur adipiscing elit, sed do eiusmod tempor incididunt ut sed quia non numquam eius modi tempora.</p>
    </article>
  </div>
</section>

<section class="about">
  <div class="abs about-photo" role="img" aria-label="Two businessmen reviewing a folder in front of a glass office building"></div>
  <div class="abs about-kicker">WELCOME TO</div>
  <h2 class="abs about-title">SERENOVA</h2>
  <div class="abs dots"><span></span><span></span><span></span><span></span><span></span><span></span></div>
  <p class="abs about-text">At vero eos et accusamus et iusto odio dignissimos ducimus qui blanditiis praesentium voluptatum deleniti atque corrupti quos dolores et quas molestias excepturi sint occaecati cupiditate non provident, similique sunt in culpa qui officia deserunt mollitia animi, id est laborum et dolorum fuga. Et harum quidem rerum facilis est et expedita distinctio.</p>
  <div class="abs features">
    <div class="feature"><svg width="34" height="34" viewBox="0 0 34 34" fill="none" stroke="var(--orange)" stroke-width="3"><path d="M22 8h-8a4 4 0 000 8h6a4 4 0 010 8h-9M17 4v26M6 6l22 22"/></svg><b>Commission</b></div>
    <div class="feature"><svg width="34" height="34" viewBox="0 0 34 34"><rect x="6" y="3" width="22" height="28" fill="var(--orange)"/><path d="M11 11h12M11 17h12M11 23h7" stroke="#fff" stroke-width="2.5"/></svg><b>No hidden fees</b></div>
    <div class="feature"><svg width="40" height="34" viewBox="0 0 40 34" fill="var(--orange)"><rect x="2" y="20" width="16" height="5"/><rect x="2" y="27" width="16" height="5"/><rect x="20" y="13" width="16" height="5"/><rect x="20" y="20" width="16" height="5"/><rect x="20" y="27" width="16" height="5"/><rect x="20" y="6" width="16" height="5"/></svg><b>Any size debt</b></div>
    <div class="feature"><svg width="34" height="34" viewBox="0 0 34 34" fill="none" stroke="var(--orange)" stroke-width="3"><circle cx="17" cy="17" r="13"/><path d="M17 9v8l6 4"/></svg><b>Instant action</b></div>
    <div class="feature"><svg width="34" height="34" viewBox="0 0 34 34"><circle cx="17" cy="17" r="14" fill="none" stroke="var(--orange)" stroke-width="3"/><text x="17" y="22" text-anchor="middle" font-family="Poppins,sans-serif" font-weight="700" font-size="12" fill="var(--orange)">24</text></svg><b>24/7 Support</b></div>
    <div class="feature"><svg width="34" height="34" viewBox="0 0 34 34" fill="var(--orange)"><circle cx="14" cy="10" r="7"/><rect x="3" y="20" width="22" height="12"/><circle cx="25" cy="14" r="5"/></svg><b>Experts</b></div>
  </div>
</section>

<section class="articles">
  <h2 class="heading">ARTICLES</h2>
  <div class="dots"><span></span><span></span><span></span><span></span><span></span><span></span></div>
  <div class="article-grid">
    <article class="article-card">
      <div class="article-img a1" role="img" aria-label="Family running across a field at sunset"></div>
      <span class="article-date">03 March,2019</span>
      <div class="article-body"><h3>On the other hand we denou nce with righte</h3><p>At vero eos et accusamus et iusto odio dignissimos ducimus qui blanditiis praesentium us indignation.</p><a class="btn">Read More</a></div>
    </article>
    <article class="article-card">
      <div class="article-img a2" role="img" aria-label="Group of business people in silhouette in a bright office hall"></div>
      <span class="article-date">03 March,2019</span>
      <div class="article-body"><h3>On the other hand we denou nce with righte</h3><p>At vero eos et accusamus et iusto odio dignissimos ducimus qui blanditiis praesentium us indignation.</p><a class="btn">Read More</a></div>
    </article>
    <article class="article-card">
      <div class="article-img a3" role="img" aria-label="Meeting around a table in a modern glass-walled office"></div>
      <span class="article-date">03 March,2019</span>
      <div class="article-body"><h3>On the other hand we denou nce with righte</h3><p>At vero eos et accusamus et iusto odio dignissimos ducimus qui blanditiis praesentium us indignation.</p><a class="btn">Read More</a></div>
    </article>
  </div>
</section>

<section class="testimonials">
  <h2 class="heading">TESTIMONIALS</h2>
  <div class="dots"><span></span><span></span><span></span><span></span><span></span><span></span></div>
  <svg class="abs arrow-l" width="20" height="30"><path d="M16 3L4 15l12 12" fill="none" stroke="#aaa" stroke-width="2.5"/></svg>
  <svg class="abs arrow-r" width="20" height="30"><path d="M4 3l12 12L4 27" fill="none" stroke="#aaa" stroke-width="2.5"/></svg>
  <div class="abs quote-open">“</div>
  <p class="abs quote">At vero eos et accusamus et iusto odio dignissimos ducimus qui blanditiis praesentium voluptatum deleniti atque corrupti quos dolores et quas molestias excepturi sint occaecati cupiditate non provident, similique sunt in culpa qui officia deserunt mollitia animi, id est laborum et dolorum fuga. Et harum quidem rerum facilis est et expedita distinctio. Lorem Ipsum which looks reasonable. The generated Lorem Ipsum is therefore always free from</p>
  <div class="abs quote-close">”</div>
  <div class="abs who"><b>DANIEL</b>Los Angels</div>
</section>

<section class="cta">
  <div class="cta-photo" role="img" aria-label="Faded photo of a family running in a field"></div>
  <p class="abs cta-line1">At vero eos et accusamus et iusto odio dignissimos</p>
  <p class="abs cta-line2">ducimus qui blanditiis praesentium.</p>
  <a class="abs btn">Contact Us</a>
</section>

<footer class="footer">
  <svg class="abs footer-deco" width="300" height="340"><polygon points="120,40 200,0 200,340 120,340" fill="rgba(255,255,255,.05)"/><polygon points="210,60 300,20 300,340 210,340" fill="rgba(255,255,255,.04)"/></svg>
  <div class="abs footer-brand">
    <div class="brand-name"><i></i>SERENOVA</div>
    <div class="brand-tag">Your guarantee of calm</div>
  </div>
  <div class="abs fcol" style="left:447px">
    <h4>CONTACT US</h4>
    <div class="row"><svg width="10" height="14" viewBox="0 0 10 14"><path d="M5 0a5 5 0 015 5c0 4-5 9-5 9S0 9 0 5a5 5 0 015-5z" fill="#fff"/></svg><span>Kastanjelaan 42<br>3800 AB Meerdorp, The Netherlands</span></div>
    <div class="row"><svg width="12" height="12" viewBox="0 0 24 24"><path fill="#fff" d="M6.6 10.8a15 15 0 006.6 6.6l2.2-2.2c.3-.3.7-.4 1-.2 1.1.4 2.3.6 3.6.6.6 0 1 .4 1 1V20c0 .6-.4 1-1 1A17 17 0 013 4c0-.6.4-1 1-1h3.5c.6 0 1 .4 1 1 0 1.3.2 2.5.6 3.6.1.3 0 .7-.2 1z"/></svg><span>800.555.0199</span></div>
    <div class="row"><svg width="12" height="10" viewBox="0 0 12 10"><rect width="12" height="10" fill="#fff"/><path d="M0 0l6 5 6-5" stroke="#0f2b5e" fill="none"/></svg><span>info@serenova.com</span></div>
  </div>
  <div class="abs fcol" style="left:745px">
    <h4>MENU</h4>
    HOME<br>ABOUT US<br>SERVICES<br>COMPLIANCE<br>BLOG<br>CONTACT US
  </div>
  <div class="abs fcol" style="left:940px">
    <h4>CONNECT WITH US</h4>
    <div class="soc"><i></i>Friendbook</div>
    <div class="soc"><i></i>Chirper</div>
    <div class="soc"><i></i>Linkwork</div>
  </div>
  <div class="abs footer-rule"></div>
  <p class="abs copyright">Copyrights © 2019 All Rights Reserved</p>
</footer>

</body>
</html>
```